International Food Manufacturer in the need of a new business card and logo.

Our Company - Northgate Pantry Ltd.

Our Industry - Food and Drink

We are a Wild Harvested Food Distributor / Manufacturer. We service the following food sectors: Supermarkets, Hotels, Restaurants, Cafes, Catering and all people looking to eat healthy food products.

Slogan - The foremost source for everything healthy

Business card details -

48-52 Marlow Lane
Hatherby Green
London
EC9Z 4RT United Kingdom
Dennis Prowle
+44 7000 481736 - UK
+971 50 7739205 - UAE
+38 063 914 2758 - Ukraine
dennis@northgatepantry.example
www.northgatepantry.example

Goal - We are looking for a dynamic modern new look for our corporate image and a designer who can bring this new concept to our future food product designs. Please try to incorporate 3d hexagonal vector Imaging in your design concepts.

Target Market(s)

Industry/Entity Type

Food Service

Contact Information for Business Card

Northgate Pantry Ltd.
48-52 Marlow Lane
Hatherby Green
London
EC9Z 4RT United Kingdom
Dennis Prowle
+44 7000 481736 - UK
+971 50 7739205 - UAE

Font styles to use
Serif

Colors

Designer to choose colors to be used in the design.

Requirements
Must have
• Please read project description above.
Nice to have
Should not have

```html
<!DOCTYPE html>
<html lang="en">
<head>
<meta charset="utf-8">
<title>Northgate Pantry Ltd. — Business Card</title>
<link rel="stylesheet" href="https://fonts.googleapis.com/css2?family=Cormorant+Garamond:wght@500&family=Barlow:wght@500&display=swap">
<style>
  :root {
    --ink: #333333;
    --brand-serif: #3a3a3a;
    --olive: #5a6c3d;
    --leaf: #72a046;
    --icon: #6a9a45;
    --paper: #ffffff;
    --frame: #555555;
    --hex-light: #f1f1f1;
    --hex-mid: #dcdcdc;
  }
  * { margin: 0; padding: 0; box-sizing: border-box; }
  html, body { width: 1200px; height: 706px; overflow: hidden; background: var(--paper); }
  .card {
    position: relative;
    width: 1200px;
    height: 706px;
    background: var(--paper);
    border: 1.5px solid var(--frame);
    overflow: hidden;
  }
  .hex-field {
    position: absolute;
    right: 0;
    top: 0;
    width: 340px;
    height: 336px;
    background: linear-gradient(160deg, var(--hex-light) 0%, var(--hex-mid) 40%, var(--hex-light) 70%, rgba(255,255,255,0) 100%);
    clip-path: polygon(0 0, 100% 0, 100% 100%, 70% 100%, 30% 60%, 0 40%);
  }
  .brand-mark {
    position: absolute;
    left: 222px;
    top: 228px;
    width: 80px;
    height: 80px;
    border-radius: 50%;
    background: var(--leaf);
  }
  .company {
    position: absolute;
    left: 60px;
    top: 336px;
    font-family: "Cormorant Garamond", "Times New Roman", serif;
    font-weight: 500;
    color: var(--brand-serif);
    line-height: 1;
  }
  .company-line-1 { display: block; font-size: 102px; letter-spacing: 0.5px; }
  .company-line-2 { display: block; font-size: 76px; margin-top: 4px; letter-spacing: 0.5px; }
  .shapes { position: absolute; left: 0; top: 0; }
  .person-name {
    position: absolute;
    left: 57px;
    top: 589px;
    font-family: "Barlow", Arial, sans-serif;
    font-weight: 500;
    font-size: 46px;
    color: var(--paper);
    line-height: 1;
  }
  .contact {
    position: absolute;
    left: 594px;
    font-family: "Barlow", Arial, sans-serif;
    font-weight: 500;
    font-size: 35px;
    color: var(--ink);
    line-height: 53px;
    white-space: nowrap;
  }
  .address { top: 78px; }
  .phones { top: 378px; }
  .email { top: 538px; }
  .web { top: 591px; }
  .icon { position: absolute; left: 530px; }
</style>
</head>
<body>
<div class="card">
  <div class="hex-field" role="img" aria-label="Soft grey 3D hexagon pattern"></div>

  <svg class="shapes" width="1200" height="706" viewBox="0 0 1200 706" aria-hidden="true">
    <path d="M0 559 H470 Q488 559 494 580 L528 706 H0 Z" fill="var(--olive)"/>
    <path d="M524 669 H1200 V706 H534 Z" fill="var(--leaf)"/>
    <path d="M1025 669 H1090 L1118 706 H1053 Z" fill="var(--olive)"/>
    <path d="M1102 669 H1128 L1156 706 H1130 Z" fill="var(--paper)"/>
  </svg>

  <div class="brand-mark" aria-hidden="true"></div>
  <div class="company">
    <span class="company-line-1">Northgate</span>
    <span class="company-line-2">Pantry Ltd.</span>
  </div>

  <div class="person-name">Dennis Prowle</div>

  <svg class="icon" style="top:90px" width="34" height="34" viewBox="0 0 24 24" aria-hidden="true">
    <path d="M12 2C8 2 5 5 5 9c0 5 7 13 7 13s7-8 7-13c0-4-3-7-7-7zm0 9.5A2.5 2.5 0 1 1 12 6.5a2.5 2.5 0 0 1 0 5z" fill="var(--icon)"/>
  </svg>
  <div class="contact address">
    48-52 Marlow Lane<br>
    Hatherby Green<br>
    London<br>
    EC9Z 4RT<br>
    United Kingdom
  </div>

  <svg class="icon" style="top:390px" width="40" height="32" viewBox="0 0 40 32" aria-hidden="true">
    <path d="M2 9c0-5 8-7 18-7s18 2 18 7v3h-9V8H11v4H2z" fill="var(--icon)"/>
    <path d="M11 12h18l5 8v10H6V20z" fill="var(--icon)"/>
    <g fill="var(--paper)">
      <rect x="14" y="16" width="3" height="3"/><rect x="19" y="16" width="3" height="3"/><rect x="24" y="16" width="3" height="3"/>
      <rect x="14" y="21" width="3" height="3"/><rect x="19" y="21" width="3" height="3"/><rect x="24" y="21" width="3" height="3"/>
    </g>
  </svg>
  <div class="contact phones">
    +44 7000 481736 - UK<br>
    +971 50 7739205 - UAE<br>
    +38 063 914 2758 - Ukraine
  </div>

  <svg class="icon" style="top:551px" width="38" height="28" viewBox="0 0 38 28" aria-hidden="true">
    <rect x="1.5" y="1.5" width="35" height="25" fill="none" stroke="var(--icon)" stroke-width="2.5"/>
    <path d="M1.5 1.5 L19 16 L36.5 1.5 M1.5 26.5 L14 12 M36.5 26.5 L24 12" fill="none" stroke="var(--icon)" stroke-width="2.5"/>
  </svg>
  <div class="contact email">dennis@northgatepantry.example</div>

  <svg class="icon" style="top:602px" width="36" height="36" viewBox="0 0 36 36" aria-hidden="true">
    <circle cx="18" cy="18" r="16" fill="var(--icon)"/>
    <g fill="none" stroke="var(--paper)" stroke-width="1.6">
      <ellipse cx="18" cy="18" rx="7" ry="16"/>
      <line x1="18" y1="2" x2="18" y2="34"/>
      <line x1="2" y1="18" x2="34" y2="18"/>
      <path d="M5 10 H31 M5 26 H31"/>
    </g>
  </svg>
  <div class="contact web">www.northgatepantry.example</div>
</div>
</body>
</html>
```